Website refresh for BriarlineTechnest.com

I need a new fresh website with all of the information contained in briarlinetechnest.com. The website needs to be built on the wix platform as it handles my booking, calendar and email marketing. The imperative pages are Home, About, Services, Clients and Testimonials. The other pages I can recreate based on the design chosen.

Industry/Entity Type

IT Services

Coding

Coded - Design and coding required

Number of Pages Required

5+ page

Font styles to use
Serif

Colors
00AB8E
00BBA5
67D7C9
C6EFE9
E9F9F6

Requirements
Must have
• I will need to be able to edit the document using the Wix WYSIWYG platform.
Nice to have
• See drumplot.com for a look and feel.
Should not have
• n/a

```html
<!DOCTYPE html>
<html lang="en">
<head>
<meta charset="utf-8">
<title>Briarline Technest – Reliable Computer Repair Services</title>
<link href="https://fonts.googleapis.com/css2?family=Montserrat:wght@400;500;600;700;800&family=Open+Sans:wght@400;600&display=swap" rel="stylesheet">
<style>
:root{
  --teal:#00AB8E;
  --teal-2:#00BBA5;
  --teal-3:#67D7C9;
  --mint:#C6EFE9;
  --mint-pale:#E9F9F6;
  --ink:#1f2a2e;
  --muted:#5b6668;
  --white:#ffffff;
  --deep:#0b7c69;
}
*{box-sizing:border-box;margin:0;padding:0}
html,body{width:1200px;height:4616px;overflow:hidden}
body{position:relative;background:var(--white);font-family:"Open Sans",Arial,sans-serif;color:var(--ink)}
.abs{position:absolute}
h1,h2,h3,.btn,.nav a,.brand{font-family:"Montserrat",Arial,sans-serif}
.btn{display:inline-block;background:var(--teal);color:var(--white);font-weight:700;font-size:13px;letter-spacing:.5px;padding:12px 22px;border-radius:3px;text-transform:uppercase}
.btn-outline{background:var(--white);color:var(--teal);border:2px solid var(--teal)}
.section-title{font-size:30px;font-weight:800;letter-spacing:.5px;text-align:center;color:var(--ink)}

/* header */
.site-header{top:0;left:0;width:1200px;height:128px;background:var(--white);box-shadow:0 2px 8px rgba(0,0,0,.06)}
.brand{left:140px;top:34px;display:flex;align-items:center;gap:12px}
.brand-mark{width:48px;height:48px;background:var(--teal);border-radius:4px}
.brand-name{font-size:24px;font-weight:800;color:var(--teal);line-height:1.05}
.call{left:620px;top:18px;display:flex;align-items:center;gap:8px;font-family:"Montserrat",sans-serif}
.call small{display:block;font-size:10px;color:var(--muted)}
.call strong{font-size:15px;color:var(--ink)}
.header-actions{left:820px;top:20px;display:flex;gap:14px}
.header-actions .btn{padding:9px 18px;font-size:12px}
.nav{left:450px;top:80px;display:flex;gap:26px}
.nav a{font-size:13px;font-weight:600;color:var(--ink);text-decoration:none;padding:6px 10px}
.nav a.active{background:var(--teal);color:var(--white);border-radius:2px}

/* hero */
.hero{top:128px;left:0;width:1200px;height:520px;background:linear-gradient(100deg,#0e2a33 0%,#1f4a55 45%,#5c7f86 75%,#9aa9aa 100%)}
.hero-copy{left:152px;top:90px;width:560px;color:var(--white)}
.hero-copy h1{font-size:54px;font-weight:800;line-height:1.12;letter-spacing:1px}
.hero-copy p{font-size:20px;margin:22px 0 30px;line-height:1.4;color:#e5f6f3}
.hero-dots{left:560px;top:480px;display:flex;gap:10px}
.dot{width:10px;height:10px;border-radius:50%;border:2px solid var(--white)}
.dot.on{background:var(--white)}
.hero-wave{left:0;top:560px;width:1200px;height:90px}

/* services */
.services-photo{left:152px;top:800px;width:450px;height:330px;background:linear-gradient(135deg,#26323a,#0f8f80 70%,#c9ded9)}
.services-copy{left:690px;top:800px;width:360px}
.services-copy h2{font-size:30px;font-weight:800;margin-bottom:22px}
.services-copy p{font-size:14px;line-height:1.7;color:var(--muted);margin-bottom:26px}
.support-title{left:152px;top:1186px;font-size:17px;font-weight:800;font-family:"Montserrat",sans-serif}
.support-grid{left:152px;top:1232px;width:896px;display:grid;grid-template-columns:repeat(5,1fr);gap:8px}
.support-tile{height:146px;background:var(--mint-pale);border:1px solid var(--mint);display:flex;flex-direction:column;align-items:center;justify-content:center;gap:14px;text-align:center;padding:0 12px}
.support-tile span{font-size:13px;color:var(--ink);line-height:1.3}
.support-tile.featured{background:var(--teal);border-color:var(--teal);height:170px;margin-top:-12px}
.support-tile.featured span{color:var(--white)}

/* welcome */
.welcome{top:1600px;left:0;width:1200px;height:520px;background:var(--teal)}
.welcome-strip{left:0;top:0;width:1200px;height:24px;background:var(--teal-3)}
.welcome-copy{left:152px;top:90px;width:420px;color:var(--white)}
.welcome-copy h2{font-size:30px;font-weight:800;line-height:1.2;margin-bottom:26px}
.welcome-copy p{font-size:14px;line-height:1.65;margin-bottom:16px;color:#eafaf7}
.welcome-photo{left:620px;top:40px;width:470px;height:370px;background:linear-gradient(150deg,#d9e4e2,#2e7d70 55%,#17363b)}

/* testimonials */
.testimonials{top:2140px;left:0;width:1200px;height:620px;background:var(--mint-pale)}
.testimonials .section-title{position:absolute;left:0;top:70px;width:1200px}
.quotes{left:190px;top:140px;display:flex;gap:40px}
.quote-card{width:246px;height:370px;background:var(--white);box-shadow:0 4px 14px rgba(0,0,0,.08);padding:30px 26px}
.quote-mark{font-family:"Montserrat",sans-serif;font-size:60px;font-weight:800;color:var(--teal);line-height:.8;display:block;margin-bottom:20px}
.quote-card p{font-size:13px;line-height:1.6;color:var(--muted)}
.quote-card .who{margin-top:34px;font-weight:600;color:var(--ink)}
.arrow{width:38px;height:38px;border-radius:50%;background:var(--teal-3);display:flex;align-items:center;justify-content:center}
.arrow.dark{background:#555}
.t-dots{left:566px;top:550px;display:flex;gap:10px}
.t-dots .dot{border-color:var(--teal)}
.t-dots .dot.on{background:var(--teal)}

/* booking */
.booking{top:2760px;left:0;width:1200px;height:470px;background:var(--mint)}
.booking .section-title{position:absolute;left:0;top:50px;width:1200px}
.plans{left:190px;top:120px;display:flex;gap:16px}
.plan{width:193px;height:290px;background:var(--white);border-top:6px solid var(--teal);padding:26px 20px}
.plan h3{font-size:16px;font-weight:800;line-height:1.25;margin-bottom:12px}
.plan p{font-size:11.5px;line-height:1.5;color:var(--muted);min-height:54px}
.plan .tag{display:inline-block;margin-top:12px;font-size:10px;background:var(--teal);color:var(--white);padding:2px 8px;border-radius:2px}
.plan .price{font-family:"Montserrat",sans-serif;font-weight:700;font-size:18px;margin:8px 0 12px}
.plan .btn{padding:9px 14px;font-size:11px;text-transform:none}
.plan.featured{background:var(--teal);color:var(--white);margin-top:-14px;height:318px;border-top-color:var(--deep)}
.plan.featured p{color:#e7faf6}
.plan.featured .tag{background:var(--white);color:var(--teal)}
.plan.featured .btn{background:var(--white);color:var(--teal)}

/* media */
.media .section-title{position:absolute;left:0;top:3296px;width:1200px}
.video{left:200px;top:3360px;width:800px;height:470px;background:linear-gradient(180deg,#9fc7d8 0%,#d8e6e8 40%,#7e8f6b 80%,#4e5a45 100%)}
.video-title{position:absolute;left:0;top:30px;width:800px;text-align:center;font-family:"Montserrat",sans-serif;font-size:44px;font-weight:600;color:var(--white);text-shadow:0 2px 6px rgba(0,0,0,.4)}
.video-badge{position:absolute;left:20px;bottom:20px;background:var(--white);padding:12px 16px;font-family:"Montserrat",sans-serif;font-weight:800;color:var(--teal);font-size:16px}

/* clients */
.clients .section-title{position:absolute;left:0;top:3890px;width:1200px}
.clients-lead{left:0;top:3940px;width:1200px;text-align:center;font-size:13px;color:var(--muted)}
.client-row{left:140px;top:3990px;width:920px;display:flex;justify-content:space-between;align-items:center}
.client{display:flex;align-items:center;gap:8px;font-family:"Montserrat",sans-serif;font-weight:700;font-size:15px;color:#3a4a55}
.client i{display:block;width:26px;height:26px;background:var(--teal-3);border-radius:50%}

/* footer */
.site-footer{top:4190px;left:0;width:1200px;height:426px;background:var(--teal);color:var(--white)}
.f-brand{left:152px;top:60px;display:flex;align-items:center;gap:12px}
.f-brand .brand-mark{background:var(--white)}
.f-brand .brand-name{color:var(--white)}
.follow{left:152px;top:150px;font-family:"Montserrat",sans-serif;font-weight:700;font-size:15px}
.socials{left:152px;top:182px;display:flex;gap:10px}
.socials span{width:28px;height:28px;border-radius:50%;background:var(--white)}
.f-col h3{font-size:16px;font-weight:700;margin-bottom:14px}
.f-col a{display:block;color:var(--white);text-decoration:none;font-size:13px;line-height:1.75}
.f-menu{left:436px;top:60px}
.f-contact{left:590px;top:60px}
.f-contact li{list-style:none;display:flex;align-items:center;gap:10px;font-size:13px;margin-bottom:14px}
.f-map{left:800px;top:60px;width:250px;height:220px;background:linear-gradient(135deg,#eef1ee,#d9e2dc)}
.copyright{left:0;top:396px;width:1200px;height:30px;background:var(--deep);text-align:center;font-size:11px;line-height:30px;color:#dff5f1}
</style>
</head>
<body>

<header class="site-header abs">
  <div class="brand abs"><span class="brand-mark"></span><span class="brand-name">Briarline<br>Technest</span></div>
  <div class="call abs">
    <svg width="22" height="22" viewBox="0 0 24 24"><path d="M6.6 10.8a15 15 0 0 0 6.6 6.6l2.2-2.2a1 1 0 0 1 1-.25 11.4 11.4 0 0 0 3.6.57 1 1 0 0 1 1 1V20a1 1 0 0 1-1 1A17 17 0 0 1 3 4a1 1 0 0 1 1-1h3.5a1 1 0 0 1 1 1c0 1.25.2 2.45.57 3.6a1 1 0 0 1-.25 1z" fill="#00AB8E"/></svg>
    <div><small>CALL US</small><strong>833-555-0148</strong></div>
  </div>
  <div class="header-actions abs"><span class="btn">Book Online</span><span class="btn btn-outline">Login</span></div>
  <nav class="nav abs">
    <a class="active">HOME</a><a>ABOUT</a><a>MEDIA</a><a>SERVICES</a><a>CLIENTS</a><a>WE RECOMMEND</a><a>HELP NOW</a>
  </nav>
</header>

<section class="hero abs" role="img" aria-label="Technician's hands repairing a computer circuit board">
  <div class="hero-copy abs">
    <h1>RELIABLE COMPUTER REPAIR SERVICES</h1>
    <p>Fast, affordable solutions to keep your devices running smoothly.</p>
    <span class="btn">Book Online</span>
  </div>
  <div class="hero-dots abs"><span class="dot on"></span><span class="dot"></span><span class="dot"></span><span class="dot"></span></div>
</section>
<svg class="hero-wave abs" viewBox="0 0 1200 90" preserveAspectRatio="none"><path d="M0 60 C300 10 600 90 900 40 C1020 20 1120 30 1200 50 L1200 90 L0 90Z" fill="#ffffff"/></svg>

<section class="services">
  <div class="services-photo abs" role="img" aria-label="Technician working on an open desktop computer tower"></div>
  <div class="services-copy abs">
    <h2>OUR SERVICES</h2>
    <p>We specialize in providing the computer and network support critical for small and home-based Business and Residential customers to succeed in today's world. As a Managed Services Provider, Briarline Technest delivers on-demand, on-site computer and network services that are convenient, reliable and affordable. Our commitment to excellent customer service has made us one of the most respected on-site computer repair and support providers in the region.</p>
    <span class="btn">Read More</span>
  </div>
  <h3 class="support-title abs">ON-SITE TECH SUPPORT</h3>
  <div class="support-grid abs">
    <div class="support-tile"><svg width="44" height="44" viewBox="0 0 44 44" fill="none" stroke="#00AB8E" stroke-width="2"><rect x="6" y="8" width="32" height="22" rx="2"/><path d="M16 36h12M22 30v6"/></svg><span>Remote Maintenance &amp; Monitoring</span></div>
    <div class="support-tile"><svg width="44" height="44" viewBox="0 0 44 44" fill="none" stroke="#00AB8E" stroke-width="2"><circle cx="22" cy="10" r="5"/><circle cx="10" cy="34" r="5"/><circle cx="34" cy="34" r="5"/><path d="M20 15l-8 14M24 15l8 14"/></svg><span>Networking - home office / business</span></div>
    <div class="support-tile featured"><svg width="44" height="44" viewBox="0 0 44 44" fill="none" stroke="#fff" stroke-width="2"><rect x="6" y="8" width="32" height="22" rx="2"/><path d="M16 36h12M22 30v6M16 19l4 4 8-8"/></svg><span>PC support<br>&amp; installation</span></div>
    <div class="support-tile"><svg width="44" height="44" viewBox="0 0 44 44" fill="none" stroke="#00AB8E" stroke-width="2"><rect x="8" y="10" width="28" height="24" rx="3"/><circle cx="22" cy="22" r="6"/></svg><span>Hard drive<br>back up</span></div>
    <div class="support-tile"><svg width="44" height="44" viewBox="0 0 44 44" fill="none" stroke="#00AB8E" stroke-width="2"><ellipse cx="22" cy="11" rx="12" ry="4"/><path d="M10 11v22c0 2 5 4 12 4s12-2 12-4V11M10 22c0 2 5 4 12 4s12-2 12-4"/></svg><span>Data recovery</span></div>
    <div class="support-tile"><svg width="44" height="44" viewBox="0 0 44 44" fill="none" stroke="#00AB8E" stroke-width="2"><circle cx="22" cy="22" r="14"/><path d="M8 22h28M22 8c6 6 6 22 0 28M22 8c-6 6-6 22 0 28"/></svg><span>Remote support</span></div>
    <div class="support-tile"><svg width="44" height="44" viewBox="0 0 44 44" fill="none" stroke="#00AB8E" stroke-width="2"><rect x="6" y="10" width="24" height="18" rx="2"/><rect x="30" y="14" width="8" height="20" rx="1"/><path d="M12 34h12"/></svg><span>PC/Mac repair</span></div>
    <div class="support-tile"><svg width="44" height="44" viewBox="0 0 44 44" fill="none" stroke="#00AB8E" stroke-width="2"><path d="M6 10h24v14H16l-6 5v-5H6zM34 18h4v14h-4v4l-5-4H20v-4"/></svg><span>Consulting</span></div>
    <div class="support-tile"><svg width="44" height="44" viewBox="0 0 44 44" fill="none" stroke="#00AB8E" stroke-width="2"><circle cx="22" cy="22" r="6"/><path d="M22 6v6M22 32v6M6 22h6M32 22h6M11 11l4 4M29 29l4 4M33 11l-4 4M15 29l-4 4"/></svg><span>IT solutions</span></div>
    <div class="support-tile"><svg width="44" height="44" viewBox="0 0 44 44" fill="none" stroke="#00AB8E" stroke-width="2"><path d="M22 6l14 5v10c0 9-6 14-14 17-8-3-14-8-14-17V11z"/><path d="M16 22l4 4 8-8"/></svg><span>Internet security</span></div>
  </div>
</section>

<section class="welcome abs">
  <div class="welcome-strip abs"></div>
  <div class="welcome-copy abs">
    <h2>WELCOME TO<br>BRIARLINE TECHNEST</h2>
    <p>Briarline Technest is a Managed Service Provider for numerous small business in the local area. Our Managed Services include Server Monitoring and Care, Desktop Monitoring and Care as well as Security Assessments, Domination and Monitoring.</p>
    <p>We also provide on-site computer (both PC and Mac) repair and IT support to small business and residential customers. We specialize in on-site computer repair.</p>
    <span class="btn btn-outline">Read More</span>
  </div>
  <div class="welcome-photo abs" role="img" aria-label="Hands soldering a component onto a green circuit board"></div>
</section>

<section class="testimonials abs">
  <h2 class="section-title">TESTIMONIALS</h2>
  <div class="arrow abs" style="left:120px;top:300px"><svg width="14" height="14" viewBox="0 0 14 14"><path d="M9 2L4 7l5 5" stroke="#fff" stroke-width="2" fill="none"/></svg></div>
  <div class="quotes abs">
    <article class="quote-card"><span class="quote-mark">&ldquo;</span><p>Hi there, thanks so much for taking care of my computer so quickly! I just do not know what I would do without you. As luck would have it, you are the best.</p><p class="who">Dana P.</p></article>
    <article class="quote-card"><span class="quote-mark">&ldquo;</span><p>Thanks for the great work you do for us. I so appreciate you coming by. I definitely am passing off my phone, help with Timesheets, etc.</p><p>Where would we be without you?</p><p class="who">Milo R.</p></article>
    <article class="quote-card"><span class="quote-mark">&ldquo;</span><p>Transferred files from old computer to new computer and installed software. Also gave a wealth of information! Will definitely refer!</p><p class="who">Tessa K.</p></article>
  </div>
  <div class="arrow abs" style="left:1042px;top:300px"><svg width="14" height="14" viewBox="0 0 14 14"><path d="M5 2l5 5-5 5" stroke="#fff" stroke-width="2" fill="none"/></svg></div>
  <div class="t-dots abs"><span class="dot on"></span><span class="dot"></span><span class="dot"></span><span class="dot"></span></div>
</section>

<section class="booking abs">
  <h2 class="section-title">BOOK ONLINE</h2>
  <div class="arrow dark abs" style="left:80px;top:250px"><svg width="14" height="14" viewBox="0 0 14 14"><path d="M9 2L4 7l5 5" stroke="#fff" stroke-width="2" fill="none"/></svg></div>
  <div class="plans abs">
    <article class="plan featured"><h3>BUSINESS ON-SITE IT</h3><p>Technical visit to your Business/Home Office.</p><span class="tag">1 hr</span><div class="price">$125/hr</div><span class="btn">Check Availability</span></article>
    <article class="plan"><h3>BUSINESS REMOTE IT</h3><p>We can support you remotely.</p><span class="tag">1 hr</span><div class="price">$125/hr</div><span class="btn">Check Availability</span></article>
    <article class="plan"><h3>MANAGED IT ON-SITE</h3><p>On-Site Service ONLY for clients with a monthly Remote Managed Service Plan.</p><span class="tag">1 hr</span><div class="price">$150/hr</div><span class="btn">Book Now</span></article>
    <article class="plan"><h3>MANAGED IT REMOTE</h3><p>Remote Service ONLY for clients with a monthly Remote Managed Service Plan.</p><span class="tag">1 hr</span><div class="price">$100/hr</div><span class="btn">Book Now</span></article>
  </div>
  <div class="arrow dark abs" style="left:1082px;top:250px"><svg width="14" height="14" viewBox="0 0 14 14"><path d="M5 2l5 5-5 5" stroke="#fff" stroke-width="2" fill="none"/></svg></div>
</section>

<section class="media">
  <h2 class="section-title">MEDIA</h2>
  <div class="arrow dark abs" style="left:110px;top:3590px"><svg width="14" height="14" viewBox="0 0 14 14"><path d="M9 2L4 7l5 5" stroke="#fff" stroke-width="2" fill="none"/></svg></div>
  <div class="video abs" role="img" aria-label="Video still of a presenter standing in front of a garden pergola">
    <div class="video-title">Using AI in your Daily Life</div>
    <div class="video-badge">Briarline Technest</div>
  </div>
  <div class="arrow dark abs" style="left:1052px;top:3590px"><svg width="14" height="14" viewBox="0 0 14 14"><path d="M5 2l5 5-5 5" stroke="#fff" stroke-width="2" fill="none"/></svg></div>
</section>

<section class="clients">
  <h2 class="section-title">OUR CLIENTS</h2>
  <p class="clients-lead abs">We are proud to be the Managed Services Provider and/or provide Computer Repair Service for the clients below.</p>
  <div class="arrow dark abs" style="left:70px;top:4022px"><svg width="14" height="14" viewBox="0 0 14 14"><path d="M9 2L4 7l5 5" stroke="#fff" stroke-width="2" fill="none"/></svg></div>
  <div class="client-row abs">
    <span class="client"><i></i>Stillbrook</span>
    <span class="client"><i></i>Oakvale Dental</span>
    <span class="client"><i></i>Redfern Co.</span>
    <span class="client"><i></i>Pennick Home</span>
    <span class="client"><i></i>Quellmar</span>
    <span class="client"><i></i>Harrow Law Firm</span>
  </div>
  <div class="arrow dark abs" style="left:1092px;top:4022px"><svg width="14" height="14" viewBox="0 0 14 14"><path d="M5 2l5 5-5 5" stroke="#fff" stroke-width="2" fill="none"/></svg></div>
</section>

<footer class="site-footer abs">
  <div class="f-brand abs"><span class="brand-mark"></span><span class="brand-name">Briarline<br>Technest</span></div>
  <p class="follow abs">Follow us</p>
  <div class="socials abs"><span></span><span></span><span></span><span></span><span></span></div>
  <div class="f-col f-menu abs"><h3>Menu</h3><a>Home</a><a>About</a><a>Media</a><a>Services</a><a>Book Online</a><a>Clients</a><a>We Recommend</a><a>Help Now</a></div>
  <div class="f-col f-contact abs"><h3>Contact us</h3>
    <ul>
      <li><svg width="14" height="14" viewBox="0 0 24 24"><path d="M12 2a7 7 0 0 0-7 7c0 5 7 13 7 13s7-8 7-13a7 7 0 0 0-7-7zm0 9.5A2.5 2.5 0 1 1 12 6.5a2.5 2.5 0 0 1 0 5z" fill="#fff"/></svg>Cedarfield</li>
      <li><svg width="14" height="14" viewBox="0 0 24 24"><path d="M6.6 10.8a15 15 0 0 0 6.6 6.6l2.2-2.2a1 1 0 0 1 1-.25 11.4 11.4 0 0 0 3.6.57 1 1 0 0 1 1 1V20a1 1 0 0 1-1 1A17 17 0 0 1 3 4a1 1 0 0 1 1-1h3.5a1 1 0 0 1 1 1c0 1.25.2 2.45.57 3.6a1 1 0 0 1-.25 1z" fill="#fff"/></svg>833-555-0148</li>
      <li><svg width="14" height="14" viewBox="0 0 24 24"><path d="M3 5h18v14H3z M3 5l9 8 9-8" stroke="#fff" stroke-width="2" fill="none"/></svg>info@briarlinetechnest.com</li>
    </ul>
  </div>
  <div class="f-map abs" role="img" aria-label="Map of the local service area"></div>
  <div class="copyright abs">© 2024 Briarline Technest Managed Services LLC</div>
</footer>

</body>
</html>
```